Private Security Company Business Card and Logo Design

Looking for a modern conservative business card design for our new private security company Halvern Guard Partners, Inc. or HGP for short.
Private Security Services. The current logo we have is not very good and honestly would like a sharp logo for the card instead of using the one we have now. Open to ideas. I am easy just looking for something nicer then what I can personally design on cardloomix. I searched on zintrova for Security Company business cards went to images and found some nice designs that were made here.

Target Market(s)

Security Services

Industry/Entity Type

Business

Contact Information for Business Card

Halvern Guard Partners, Inc.
President, cell,office,fax,email, website,
Logo etc, whatever is needed for a standard business card
Can provide personal Information later.

Colors
0556a4
ffffff
474747

Requirements
Must have
• Modern but conservative,
Nice to have
• color choices
• Blue, white, Grey

```html
<!DOCTYPE html>
<html lang="en">
<head>
<meta charset="utf-8">
<title>Halvern Guard Partners, Inc. Business Card</title>
<link rel="stylesheet" href="https://fonts.googleapis.com/css2?family=Arimo:wght@400;700&display=swap">
<style>
  :root {
    --brand-blue: #0556a4;
    --brand-white: #ffffff;
    --brand-grey: #474747;
    --card-light: #f1f1f1;
    --backdrop: #1c1c1c;
    --text-light: #e6e6e6;
  }
  * { box-sizing: border-box; margin: 0; padding: 0; }
  html, body {
    width: 1200px;
    height: 800px;
    overflow: hidden;
    background: var(--backdrop);
    font-family: "Arimo", Arial, sans-serif;
  }
  .canvas {
    position: relative;
    width: 1200px;
    height: 800px;
  }
  .card {
    position: absolute;
    top: 240px;
    width: 520px;
    height: 320px;
    overflow: hidden;
    box-shadow: 0 12px 30px rgba(0,0,0,0.55);
  }
  .card--front { left: 50px; display: flex; }
  .card--back {
    left: 630px;
    background: var(--brand-blue);
    display: flex;
    align-items: center;
    justify-content: center;
  }

  /* front: brand side */
  .brand-panel {
    width: 290px;
    height: 100%;
    background: linear-gradient(135deg, var(--brand-white), var(--card-light));
    display: flex;
    flex-direction: column;
    align-items: center;
    justify-content: center;
    gap: 10px;
  }
  .brand-mark {
    display: flex;
    align-items: center;
    gap: 8px;
    color: var(--brand-blue);
    font-weight: 700;
    font-size: 34px;
    letter-spacing: 3px;
  }
  .brand-mark__square {
    width: 16px;
    height: 16px;
    background: var(--brand-blue);
  }
  .company-name {
    color: var(--brand-blue);
    font-weight: 700;
    font-size: 15px;
  }

  /* front: contact side */
  .contact-panel {
    flex: 1;
    height: 100%;
    background: var(--brand-grey);
    color: var(--brand-white);
    padding: 38px 24px 30px 26px;
    display: flex;
    flex-direction: column;
    justify-content: space-between;
  }
  .person-name { font-weight: 700; font-size: 19px; }
  .person-title { font-size: 13px; margin-top: 4px; color: var(--text-light); }
  .contact-list { list-style: none; font-size: 13px; line-height: 1.55; color: var(--text-light); }

  /* back */
  .back-mark {
    display: flex;
    align-items: center;
    gap: 16px;
    color: var(--brand-white);
    font-weight: 700;
    font-size: 84px;
    letter-spacing: 8px;
  }
  .back-mark__square {
    width: 34px;
    height: 34px;
    background: var(--brand-white);
  }
</style>
</head>
<body>
<main class="canvas">
  <section class="card card--front" aria-label="Business card front">
    <div class="brand-panel">
      <div class="brand-mark"><span class="brand-mark__square"></span>HGP</div>
      <p class="company-name">Halvern Guard Partners, Inc.</p>
    </div>
    <div class="contact-panel">
      <div class="person">
        <p class="person-name">Your Name</p>
        <p class="person-title">President</p>
      </div>
      <ul class="contact-list">
        <li>p: 0123456789</li>
        <li>f : 0123456789</li>
        <li>e: yourname@mailvane.com</li>
        <li>w: www.halvernguard.com</li>
      </ul>
    </div>
  </section>

  <section class="card card--back" aria-label="Business card back">
    <div class="back-mark"><span class="back-mark__square"></span>HGP</div>
  </section>
</main>
</body>
</html>
```